Modern Small Law Firm Website To Look Cutting Edge

I need a website design for a new, single-attorney law firm. The firm will be called "The Ashcombe Law Group." Our goal is to handle car accident and general personal injury lawsuits for individuals.

Our selling points are: (1) We charge less so you keep more; (2) We have experience and success trying and settling multi-million dollar cases; (3) We use modern technology to make the whole process simple, easy and hassle-free for clients.

Also because we are a one-man law firm, the clients will personally know the lawyer and have access to them. For that reason, I thought a good big tagline for the website would be "KNOW YOUR LAWYER"

I like the idea of splitting the website vertically down the middle, with the left side having a blue background, a picture of me, and big white lettering for the tagline, and the right side having a white background with blue lettering and headlines. I don't want navy blue or royal blue, but a more bright and eye-catching blue color. We can experiment with different shades.

I would be curious about how it could look with some minor orange accent coloring somewhere.

I need to feature prominently, probably in the top left corner, this phone number: 504-271-9038.

This will be used as much by mobile users as it would be by desktop/computer users.

The final design should communicate trust, convenience and cutting edge technology that leads to success.

Finally, I would be curious how we can have a sleek looking info submission box somewhere on the right side nearer the bottom that features different combinations of presenting these phrases: "QUICK QUESTION? QUICK ANSWER" The info submission button could say "Ask"

I am uploading two different pictures of me that can be used. The gray backgrounds are not necessary or good, if there is a way to cut them out that would be great. I can try and get that if needed.

Target Market(s)

Individuals who have been hurt by others, mostly in car accidents. They will be frustrated, inconvenienced and need to be soothed.

Industry/Entity Type

Legal

Number of Pages Required

1 page

Font styles to use
Sans Serif

Colors
0692cd
33a6d7
85cae6
faa54b
f78f20
3276b5

Requirements
Must have
• If you have started designing already, please note that the project description information is more important than the image that I uploaded originally. It has since been deleted.
• Also please now use the color photo that has been uploaded.
Nice to have
• I really want a clean and simple website design with not a lot of clutter. I'd like to avoid the typical law firm websites that you see that have tool bars across the top and basic borders/columns everywhere. It needs to grab your attention and look a little more cutting edge and different.
• Let's experiment with different eye-catching ways to present the three value propositions I noted.
• Also if the screen is split vertically with the left and right side being blue and white, maybe we can experiment with different ways that the two colors could fade into each other as opposed to just a line where one color starts and the other ends.
• And maybe the blue/white backgrounds could be textured somehow so that they don't appear flat. Perhaps we could try using differing shades of blue to give the appearance of pattern or 3D texture.
Should not have
• The basic picture/design I uploaded is just a suggestion, but there isn't really anything there.

```html
<!DOCTYPE html>
<html lang="en">
<head>
<meta charset="utf-8">
<title>The Ashcombe Law Group</title>
<link href="https://fonts.googleapis.com/css2?family=Oswald:wght@300;400;500&family=Open+Sans:wght@400;600;700&family=Montserrat:wght@400;500&display=swap" rel="stylesheet">
<style>
:root{
  --sky:#85cae6;
  --nav:#7cc3e3;
  --blue:#0692cd;
  --blue-mid:#33a6d7;
  --blue-deep:#3276b5;
  --orange:#f78f20;
  --orange-soft:#faa54b;
  --navy:#1c3857;
  --navy-deep:#14283f;
  --paper:#ecebe8;
  --beige:#ece6dc;
  --ink:#3a3a3a;
  --muted:#6b6b6b;
  --white:#ffffff;
}
*{margin:0;padding:0;box-sizing:border-box}
html,body{width:719px;height:1200px;overflow:hidden;background:var(--white)}
body{position:relative;font-family:'Open Sans',sans-serif;color:var(--ink)}
.abs{position:absolute}

/* navigation */
.site-nav{left:0;top:0;width:719px;height:24px;background:var(--nav);z-index:3}
.site-nav ul{list-style:none;display:flex;justify-content:center;gap:19px;padding-top:6px}
.site-nav li{font-family:'Oswald',sans-serif;font-weight:300;font-size:9.5px;color:var(--white);letter-spacing:.2px}

/* hero */
.hero{left:0;top:24px;width:719px;height:306px;background:radial-gradient(ellipse at 70% 40%,#8a7a68 0%,#5b564f 35%,#3b3e44 70%,#2b3038 100%)}
.hero-title{left:131px;top:160px;font-family:'Oswald',sans-serif;font-weight:400;font-size:22px;color:var(--white);letter-spacing:.3px}
.hero-text{left:132px;top:193px;width:245px;font-size:8.3px;line-height:12px;color:#f1f1f1}

.call-tab{left:136px;top:24px;width:114px;height:37px;background:var(--blue);border-radius:0 0 0 16px;color:var(--white);text-align:center;z-index:2}
.call-tab small{display:block;font-family:'Oswald',sans-serif;font-weight:300;font-size:7px;margin-top:6px}
.call-tab strong{display:block;font-family:'Oswald',sans-serif;font-weight:400;font-size:14px;line-height:15px}
.social-tab{left:470px;top:24px;width:114px;height:37px;background:var(--blue);border-radius:0 0 16px 0;z-index:2;display:flex;gap:3px;padding:10px 0 0 28px}
.social-tab span,.social-row span{width:14px;height:14px;border:1.3px solid var(--white);border-radius:50%;display:block}
.brand-tab{left:240px;top:24px;width:230px;height:63px;z-index:3}
.brand-name{left:240px;top:40px;width:230px;text-align:center;font-family:'Oswald',sans-serif;font-weight:400;font-size:16px;color:var(--blue);z-index:4}
.brand-tag{left:240px;top:61px;width:230px;text-align:center;font-size:7.5px;color:#6a6a6a;z-index:4}

/* side panels */
.side-left{left:0;top:330px;width:126px;height:660px;background:linear-gradient(180deg,#8dcdea 0%,#7ec5e6 60%,#7fc6e6 100%)}
.side-left-photo{left:54px;top:340px;width:72px;height:130px;background:linear-gradient(180deg,#a9d6ec,#8ec9e6);opacity:.8;border-radius:30px 0 0 0}
.side-right{left:593px;top:330px;width:126px;height:660px;background:linear-gradient(180deg,#f2f2f2,#e9e9e9)}
.vertical-word{width:540px;height:60px;font-family:'Montserrat',sans-serif;font-weight:400;font-size:49px;line-height:60px;text-align:center;letter-spacing:2px;white-space:nowrap}
.vertical-left{left:-208px;top:610px;transform:rotate(-90deg);color:var(--white)}
.vertical-right{left:386px;top:610px;transform:rotate(90deg);color:var(--sky)}

/* main card */
.content-frame{left:126px;top:325px;width:467px;height:671px;background:var(--white);box-shadow:0 0 6px rgba(0,0,0,.15)}

.work{left:132px;top:330px;width:455px;height:294px;background:var(--paper)}
.work-band{left:132px;top:534px;width:455px;height:90px}
.section-head{text-align:center;width:455px;left:132px}
.section-head h2{font-family:'Oswald',sans-serif;font-weight:400;font-size:15px;letter-spacing:3px;color:#222}
.section-head h2 .stars{font-size:8px;color:#9a9a9a;letter-spacing:1px;vertical-align:middle;margin:0 6px}
.section-head p{font-family:'Oswald',sans-serif;font-weight:300;font-size:8px;color:#333;letter-spacing:.3px;margin-top:-2px}

.value-card{top:404px;width:135px;height:150px;background:var(--white);border-radius:4px;box-shadow:0 1px 3px rgba(0,0,0,.2);text-align:center;overflow:hidden}
.value-card .wash{position:absolute;left:0;top:0;width:135px;height:60px;background:linear-gradient(180deg,#f6e8d6,#fbf3ea 70%,#fff)}
.value-card .badge{position:absolute;left:42px;top:-9px;width:52px;height:52px;border-radius:50%;background:var(--white);box-shadow:0 1px 3px rgba(0,0,0,.2)}
.value-card .badge svg{position:absolute;left:4px;top:4px}
.value-card h3{position:absolute;top:66px;width:135px;font-family:'Oswald',sans-serif;font-weight:300;font-size:11px;color:#222}
.value-card h4{position:absolute;top:80px;width:135px;font-weight:400;font-size:6.5px;color:#777}
.value-card p{position:absolute;top:97px;left:9px;width:117px;font-size:6.3px;line-height:10.5px;color:#555}

.about-head h2{color:var(--white)}
.about-head h2 .stars{color:#a6c9e8}
.about-head p{color:var(--white)}
.about{left:132px;top:608px;width:455px;height:138px;background:var(--beige)}
.about-photo{left:156px;top:620px;width:104px;height:126px;background:linear-gradient(180deg,#e4ddd1 0%,#54565c 45%,#26282d 100%);border-radius:40px 40px 0 0}
.about-text{left:276px;top:652px;width:284px;font-size:6.4px;line-height:10.3px;color:#555}

.features{left:132px;top:746px;width:455px;height:244px;background:linear-gradient(180deg,#a9cfcc 0%,#bcd8d4 40%,#cfe0dc 100%)}
.feature-card{top:818px;width:104px;height:142px}
.feature-card .sheet{position:absolute;left:0;top:28px;width:104px;height:114px;background:var(--white);box-shadow:2px 2px 4px rgba(0,0,0,.2)}
.feature-card .tab{position:absolute;left:4px;top:0;width:100px;height:40px;background:#1e3045;clip-path:polygon(0 0,100% 12%,100% 100%,0 100%)}
.feature-card .tab svg{position:absolute;left:8px;top:8px}
.feature-card h3{position:absolute;left:9px;top:50px;font-family:'Oswald',sans-serif;font-weight:300;font-size:11px;line-height:12.5px;color:#222}
.feature-card p{position:absolute;left:9px;top:82px;width:90px;font-size:6.2px;line-height:10.3px;color:#666}

/* footer */
.footer{left:0;top:990px;width:719px;height:191px;background:linear-gradient(180deg,#1e4063,#1a3656)}
.footer-photo{left:490px;top:1000px;width:130px;height:181px;background:linear-gradient(180deg,rgba(60,90,125,.5),rgba(40,65,95,.4));border-radius:50px 50px 0 0}
.ask-title{left:240px;top:1007px;font-family:'Oswald',sans-serif;font-weight:400;font-size:15px;color:var(--white)}
.ask-btn{left:438px;top:1009px;width:40px;height:18px;border-radius:9px;background:var(--orange);color:var(--white);font-family:'Oswald',sans-serif;font-size:10px;line-height:18px;text-align:center}
.foot-col{top:1043px}
.foot-col h5{font-family:'Oswald',sans-serif;font-weight:300;font-size:8px;color:var(--white);padding-bottom:5px;border-bottom:1px solid rgba(255,255,255,.2);width:97px}
.quick-links{list-style:none;margin-top:8px}
.quick-links li{font-size:6.2px;color:#e4ecf4;line-height:13.6px}
.contact-item{position:absolute;left:19px;font-size:5.6px;color:#d8e2ee;line-height:9.3px}
.contact-item b{display:block;font-size:6.2px;color:var(--white)}
.contact-icon{position:absolute;left:0}
.field{width:97px;height:17px;background:#eef0f2;border-radius:3px;font-size:6.2px;color:#555;padding:4px 7px;margin-top:6px}
.subscribe{width:97px;height:17px;background:var(--orange);border-radius:3px;font-size:6.8px;font-weight:700;color:var(--white);text-align:center;line-height:17px;margin-top:5px}
.social-row{display:flex;gap:3px;margin-top:9px}
.social-row span{width:15px;height:15px}
.copyright{left:0;top:1181px;width:719px;height:19px;background:var(--navy-deep);text-align:center;font-size:5.6px;color:#b7c3d0;line-height:19px}
</style>
</head>
<body>

<nav class="site-nav abs">
  <ul><li>HOME</li><li>ABOUT MY FIRM</li><li>ATTORNEY BIO</li><li>PERSONAL INJURY</li><li>TESTIMONIALS</li><li>BLOG</li><li>CONTACT</li></ul>
</nav>

<header class="hero abs" role="img" aria-label="Bronze statue of Lady Justice holding scales against a dusk sky"></header>

<div class="call-tab abs"><small>CALL NOW</small><strong>504-271-9038</strong></div>
<div class="social-tab abs"><span></span><span></span><span></span><span></span></div>
<svg class="brand-tab abs" width="230" height="63" viewBox="0 0 230 63">
  <path d="M0 0 H230 L214 50 Q210 60 196 60 Q115 66 34 60 Q20 60 16 50 Z" fill="#f3f3f3"/>
</svg>
<div class="brand-name abs">THE ASHCOMBE LAW GROUP</div>
<div class="brand-tag abs">Your Injury Case Is Important</div>

<h1 class="hero-title abs">KNOW YOUR LAWYER</h1>
<p class="hero-text abs">At Ashcombe Law Firm, you will talk to your lawyer on your first call. No screener, no receptionist, just instant advice. You will know your lawyer.</p>

<aside class="side-left abs"></aside>
<div class="side-left-photo abs" role="img" aria-label="Portrait of the attorney in a suit, tinted blue"></div>
<div class="vertical-word vertical-left abs">KNOW YOUR LAWYER</div>
<aside class="side-right abs"></aside>
<div class="vertical-word vertical-right abs">KNOW YOUR LAWYER</div>

<div class="content-frame abs"></div>

<section class="work abs"></section>
<svg class="work-band abs" width="455" height="90" viewBox="0 0 455 90">
  <path d="M0 6 L455 0 V72 L285 72 L227 88 L170 72 L0 72 Z" fill="var(--blue-deep)"/>
  <line x1="75" y1="50" x2="160" y2="50" stroke="#5b94c8" stroke-width="1"/>
  <line x1="295" y1="50" x2="380" y2="50" stroke="#5b94c8" stroke-width="1"/>
</svg>

<div class="section-head abs" style="top:352px">
  <h2><span class="stars">★★★</span>HOW WE WORK<span class="stars">★★★</span></h2>
  <p>OUR VALUE TO YOU</p>
</div>

<article class="value-card abs" style="left:144px">
  <div class="wash"></div>
  <div class="badge"><svg width="44" height="44" viewBox="0 0 44 44"><circle cx="22" cy="22" r="22" fill="var(--blue)"/><circle cx="22" cy="16" r="5" fill="none" stroke="#fff" stroke-width="1.5"/><circle cx="28" cy="21" r="3.5" fill="none" stroke="#fff" stroke-width="1.5"/><path d="M11 27 h7 l6 3 h7 M11 27 v6 h6 l7 2 l9 -5" fill="none" stroke="#fff" stroke-width="1.6" stroke-linejoin="round"/></svg></div>
  <h3>CHARGE LESS</h3><h4>YOUR CASE, YOUR MONEY</h4>
  <p>Our law firm is structured to make sure that we charge less so you can keep more. Call and ask us about how we do it.</p>
</article>
<article class="value-card abs" style="left:292px">
  <div class="wash"></div>
  <div class="badge"><svg width="44" height="44" viewBox="0 0 44 44"><circle cx="22" cy="22" r="22" fill="var(--blue-mid)"/><path d="M8 19 L22 13 L36 19 L22 25 Z" fill="#fff"/><path d="M14 22 V29 Q22 33 30 29 V22 L22 26 Z" fill="#fff"/></svg></div>
  <h3>EXPERIENCE</h3><h4>HISTORY OF SUCCESS</h4>
  <p>Through trial or settlement, we have successfully recovered hundreds of thousands of dollars for our clients.</p>
</article>
<article class="value-card abs" style="left:440px">
  <div class="wash"></div>
  <div class="badge"><svg width="44" height="44" viewBox="0 0 44 44"><circle cx="22" cy="22" r="22" fill="var(--sky)"/><rect x="14" y="10" width="16" height="23" rx="2" fill="none" stroke="#fff" stroke-width="1.6"/><rect x="17" y="13" width="10" height="14" fill="none" stroke="#fff" stroke-width="1"/><circle cx="22" cy="30.5" r="1" fill="#fff"/></svg></div>
  <h3>TECHNOLOGY</h3><h4>WE MAKE THIS EASY</h4>
  <p>Our law firm uses the most cutting edge technologyto work on your terms, your schedule, and always be accessible.</p>
</article>

<div class="section-head about-head abs" style="top:574px">
  <h2><span class="stars">★★★</span>ABOUT US<span class="stars">★★★</span></h2>
  <p>THE BOTTOM LINE</p>
</div>

<section class="about abs"></section>
<div class="about-photo abs" role="img" aria-label="Photo of the attorney standing in a dark suit and tie"></div>
<p class="about-text abs">Our law firm was created with one philosophy: to do great work for our clients and not overcharge them for it. Lawyers on TV need to charge big fees so that they can run commercials. The bigger the billboard, the bigger the bill for the client. By using only the most cutting edge digital technology and avoiding traditional legal marketing, our firm has created savings that we pass along directly to our clients. The bottom line: with us you get to keep more of your money.</p>

<section class="features abs" role="img" aria-label="Faded courthouse columns behind the features"></section>
<div class="section-head abs" style="top:766px">
  <h2 style="color:#fff"><span class="stars" style="color:#eef">★★★</span>OUR FEATURES<span class="stars" style="color:#eef">★★★</span></h2>
  <p style="color:#fff">OUR PROCESS WORKS FOR YOU</p>
</div>

<article class="feature-card abs" style="left:170px">
  <div class="tab"><svg width="30" height="24" viewBox="0 0 30 24"><rect x="1" y="2" width="15" height="10" rx="4" fill="var(--orange)"/><rect x="11" y="9" width="15" height="10" rx="4" fill="var(--orange)"/><path d="M20 18 l3 5 l0 -5z" fill="var(--orange)"/><circle cx="15" cy="14" r="1" fill="#1e3045"/><circle cx="19" cy="14" r="1" fill="#1e3045"/><circle cx="23" cy="14" r="1" fill="#1e3045"/></svg></div>
  <div class="sheet"></div>
  <h3>FREE<br>CONSULTATION</h3>
  <p>It's always free to reach out to us and talk. Let's see how we can help.</p>
</article>
<article class="feature-card abs" style="left:310px">
  <div class="tab"><svg width="30" height="24" viewBox="0 0 30 24"><rect x="8" y="2" width="20" height="12" fill="none" stroke="var(--orange)" stroke-width="1.6"/><rect x="2" y="8" width="20" height="12" fill="#1e3045" stroke="var(--orange)" stroke-width="1.6"/><circle cx="12" cy="14" r="3" fill="none" stroke="var(--orange)" stroke-width="1.5"/></svg></div>
  <div class="sheet"></div>
  <h3>NO FEE UNLESS<br>WE WIN</h3>
  <p>The way we structure our fees, we never get paid unless you do too.</p>
</article>
<article class="feature-card abs" style="left:445px">
  <div class="tab"><svg width="30" height="24" viewBox="0 0 30 24"><circle cx="6" cy="5" r="2.5" fill="var(--orange)"/><path d="M3 9 h6 v8 h-1 v6 h-4 v-6 h-1z" fill="var(--orange)"/><rect x="12" y="3" width="15" height="11" fill="none" stroke="var(--orange)" stroke-width="1.5"/><path d="M15 23 l4 -9 l4 9" fill="none" stroke="var(--orange)" stroke-width="1.5"/><path d="M9 10 l5 -3" stroke="var(--orange)" stroke-width="1.2"/></svg></div>
  <div class="sheet"></div>
  <h3>PERSONAL<br>REPRESENTATION</h3>
  <p>Unlike the lawyer on the billboard, you'll know us personally.</p>
</article>

<footer class="footer abs"></footer>
<div class="footer-photo abs" role="img" aria-label="Faded portrait of the attorney in the footer background"></div>
<h2 class="ask-title abs">QUICK QUESTION? QUICK ANSWER</h2>
<div class="ask-btn abs">ASK</div>

<div class="foot-col abs" style="left:144px">
  <h5>QUICK LINKS</h5>
  <ul class="quick-links"><li>Home</li><li>About My Firm</li><li>Attorney Bio</li><li>Personal Injury</li><li>Testimonials</li><li>Blog</li><li>Contact</li></ul>
</div>
<div class="foot-col abs" style="left:255px;width:120px;height:130px">
  <h5>GET IN TOUCH NOW!</h5>
  <svg class="contact-icon" style="top:23px" width="13" height="13" viewBox="0 0 13 13"><path d="M6.5 1 a4 4 0 0 1 4 4 c0 3 -4 7 -4 7 s-4 -4 -4 -7 a4 4 0 0 1 4 -4z" fill="none" stroke="#cfd9e5" stroke-width="1.3"/><circle cx="6.5" cy="5" r="1.4" fill="#cfd9e5"/></svg>
  <div class="contact-item" style="top:25px"><b>ADDRESS</b>Your Company LTD.<br>Street Name, 000000<br>City Name</div>
  <svg class="contact-icon" style="top:73px" width="12" height="12" viewBox="0 0 12 12"><path d="M2 1 l2.5 0 l1 3 l-1.5 1 q1 2 3 3 l1 -1.5 l3 1 v2.5 q-6 1 -9 -9z" fill="#cfd9e5"/></svg>
  <div class="contact-item" style="top:73px"><b>PHONE</b>504-271-9038</div>
  <svg class="contact-icon" style="top:102px" width="13" height="10" viewBox="0 0 13 10"><rect x=".5" y=".5" width="12" height="9" fill="#cfd9e5"/><path d="M.5 .5 l6 5 l6 -5" fill="none" stroke="#1d3b5c" stroke-width="1"/></svg>
  <div class="contact-item" style="top:102px"><b>EMAIL</b>info@yourdomain.com</div>
</div>
<div class="foot-col abs" style="left:367px">
  <h5>SUBSCRIBE NEWSLETTER</h5>
  <div class="field" style="margin-top:14px">Name</div>
  <div class="field">Email</div>
  <div class="subscribe">SUBSCRIBE</div>
</div>
<div class="foot-col abs" style="left:478px">
  <h5>CONNECT WITH US</h5>
  <div class="social-row"><span></span><span></span><span></span><span></span></div>
</div>

<div class="copyright abs">© 2016 THE ASHCOMBE LAW GROUP. ALL RIGHTS RESERVED | DISCLAIMER | SITE MAP | PRIVACY POLICY</div>

</body>
</html>
```